Need 3 posters for in-store display

Hi Marla,

Hope you are well.
I need 3 posters for display in my restaurant.

Poster 1: To be print in A1 size vertical
Title: BOWL-ERIFIC DEAL $19.50
Choose any Pho OR Noodle Salads
Choose Spring Rolls (5 rolls) OR Ricepaper Rolls (2 rolls)
Choose any Cans OR Water

What I like to see:
- These poster will be place near my counter so I want it to grab customer attention.
- You must use photos to show products
- Make it easy to understand and for customer to follow

Poster 2: To be print in A4 size vertical
Title: ADD TO YOUR ORDER
SpringRolls (Crab / vegetarian) $6 / 5 rolls
Extra Meat $2
Extra Noodles $1
Extra Vegs $1.5
Extra Tofu $2
Extra Crackling $3

Poster 3: To be print in A1 size vertical
Title: BROTH BONANZA FEAST
Catering Menu Options:
- PHO (Beef, Chicken, Vegan) $12.50 per bowl
- NOODLE SALADS (Beef, Chicken, BBQ Pork, Vegan) $12.50 per bowl
- SpringRolls (Crab / vegetarian) $12.50 for 10 rolls
- Ricepaper Rolls (Prawn, Beef, Chicken, BBQ Pork, Tofu) $12.5 / 5 rolls
- Fried Rice (Prawn, Tofu) $50 per tray (serve 5-6)

Terms & Conditions for All Catering Orders:
1) Minimum orders $200 (Pick-Up from shop Only)
2) All orders must be paid upfront
3) Requires $300 bond for Soup Tank
4) Please give us 48hours notice

• For the BOWL-ERIFIC DEAL
• it would be nice to have an image of the battle of water to visually complete the meal deal
• please see attachment of the Cedar Ridge Water

```html
<!DOCTYPE html>
<html lang="en">
<head>
<meta charset="utf-8">
<title>Bowl-erific Deal – A1 Posters</title>
<link href="https://fonts.googleapis.com/css2?family=Kaushan+Script&family=Exo+2:ital,wght@1,400;1,500&family=Raleway:wght@400;500;600&display=swap" rel="stylesheet">
<style>
  :root {
    --stage: #e4e4e2;
    --gold: #f2b233;
    --ribbon: #b99c62;
    --ribbon-fold: #7d5f2c;
    --cream: #fff7e4;
    --white: #ffffff;
    --price-ink: #5a3a22;
    --badge: #efe9df;
    --ocean-mid: #2f86b0;
    --ocean-deep: #0c3249;
    --timber-mid: #7d6044;
    --timber-deep: #2b1f15;
  }
  * { box-sizing: border-box; margin: 0; padding: 0; }
  html, body { width: 1200px; height: 900px; overflow: hidden; }
  body { background: var(--stage); position: relative; font-family: "Raleway", sans-serif; }

  .poster {
    position: absolute; top: 50px; width: 622px; height: 880px;
    transform: scale(0.91); transform-origin: top left;
    overflow: hidden; color: var(--white);
    box-shadow: 0 10px 30px rgba(0,0,0,.35);
  }
  .poster--ocean { left: 22px; background: radial-gradient(ellipse at 50% 45%, var(--ocean-mid) 0%, #1d6184 55%, var(--ocean-deep) 100%); }
  .poster--timber { left: 612px; background:
      radial-gradient(ellipse at 50% 45%, rgba(0,0,0,0) 30%, rgba(0,0,0,.55) 100%),
      linear-gradient(100deg, var(--timber-mid) 0%, #6b5038 40%, #85684b 70%, #5e4532 100%); }

  .frame { position: absolute; inset: 0; width: 622px; height: 880px; }

  .title { position: absolute; font-family: "Kaushan Script", cursive; font-weight: 400; color: var(--white); line-height: 1; white-space: nowrap; text-shadow: 0 3px 6px rgba(0,0,0,.45); }
  .title__top { left: 62px; top: 18px; font-size: 68px; }
  .title__bottom { left: 170px; top: 90px; font-size: 72px; }

  .thumb { position: absolute; left: 440px; top: 70px; width: 115px; height: 120px; filter: drop-shadow(0 0 6px rgba(242,178,51,.7)); }

  .photo { position: absolute; border-radius: 50%; box-shadow: 0 8px 14px rgba(0,0,0,.35); }
  .photo--bowl { background: radial-gradient(ellipse at 50% 40%, #7a4a26 0%, #a06a36 35%, #f4f4f2 62%, #dcdcdc 100%); }
  .photo--salad { background: radial-gradient(ellipse at 50% 38%, #8a5a32 0%, #d7b878 35%, #f4f4f2 62%, #dcdcdc 100%); }
  .photo--plate { border-radius: 8px; background: linear-gradient(160deg, #f5f5f3 0%, #d9d9d6 100%); }
  .photo--plate::after { content: ""; position: absolute; left: 22%; top: 18%; width: 56%; height: 60%; border-radius: 40%; background: radial-gradient(#c7782e, #9a561c); }
  .photo--board { border-radius: 6px; background: linear-gradient(160deg, #e9e6dc 0%, #f4f1e8 45%, #b88a4c 75%, #8d632f 100%); }
  .photo--bottle { border-radius: 20px 20px 14px 14px; background: linear-gradient(90deg, #c9d9e6 0%, #ffffff 45%, #bccfdf 100%); box-shadow: 0 6px 10px rgba(0,0,0,.3); }

  .label { position: absolute; font-size: 11.5px; text-decoration: underline; color: var(--white); white-space: nowrap; }
  .poster--timber .label { background: rgba(120,90,60,.85); padding: 1px 4px; }

  .ribbon { position: absolute; height: 46px; background: var(--ribbon); font-family: "Exo 2", sans-serif; font-style: italic; font-weight: 500; font-size: 33px; line-height: 46px; color: var(--cream); text-align: center; white-space: nowrap; text-shadow: 0 2px 3px rgba(0,0,0,.35); }
  .ribbon__fold { position: absolute; top: 46px; width: 0; height: 0; border-top: 24px solid var(--ribbon-fold); }
  .ribbon__fold--right { right: 0; border-left: 58px solid transparent; }
  .ribbon__fold--left { left: 0; border-right: 58px solid transparent; }
  .ribbon--mains { left: 363px; top: 215px; width: 208px; }
  .ribbon--sides { left: 38px; top: 508px; width: 208px; }
  .ribbon--drinks { left: 275px; top: 728px; width: 208px; }

  .choice { position: absolute; white-space: nowrap; text-shadow: 0 2px 3px rgba(0,0,0,.35); }
  .choice--or { color: var(--gold); font-weight: 500; font-size: 56px; line-height: 1; }
  .choice--pho { left: 372px; top: 286px; font-size: 38px; line-height: 56px; }
  .choice--salads { left: 400px; top: 350px; width: 146px; white-space: normal; text-align: right; font-size: 33px; line-height: 32px; }
  .choice--spring { left: 37px; top: 584px; font-size: 22px; line-height: 27px; }
  .choice--spring-count { left: 68px; top: 611px; font-size: 22px; line-height: 27px; }
  .choice--sides-or { left: 160px; top: 608px; }
  .choice--ricepaper { left: 262px; top: 632px; font-size: 22px; line-height: 27px; }
  .choice--ricepaper-count { left: 310px; top: 659px; font-size: 22px; line-height: 27px; }
  .count { color: var(--gold); }

  .drinks { position: absolute; left: 230px; top: 797px; font-family: "Exo 2", sans-serif; font-style: italic; font-size: 35px; white-space: nowrap; color: var(--gold); text-shadow: 0 2px 3px rgba(0,0,0,.35); }
  .drinks__or { color: var(--white); }

  .price { position: absolute; left: 55px; top: 740px; width: 150px; height: 96px; border-radius: 50%; background: var(--badge); border: 2px dashed #b9b2a6; outline: 4px solid var(--badge); display: flex; align-items: center; justify-content: center; font-family: "Raleway", sans-serif; font-weight: 600; font-size: 33px; color: var(--price-ink); }

  .guides { position: absolute; inset: 0; width: 622px; height: 880px; pointer-events: none; }
</style>
</head>
<body>

<section class="poster poster--ocean" aria-label="Bowl-erific Deal poster, blue edition">
  <svg class="frame" viewBox="0 0 622 880" aria-hidden="true">
    <path d="M50 45 H15 V853 H608 V45 H432" fill="none" stroke="#fff" stroke-width="3"/>
  </svg>
  <h1 class="title title__top">Bowl-erific</h1>
  <p class="title title__bottom">Deal</p>
  <svg class="thumb" viewBox="0 0 115 120" aria-hidden="true">
    <path d="M10 55 H38 L55 18 C58 8 72 8 72 22 L68 45 H100 C110 45 112 58 104 62 C112 66 110 78 101 79 C108 83 106 95 97 95 C102 100 98 110 90 110 H45 L38 104 H10 Z" fill="none" stroke="#f2b233" stroke-width="5" stroke-linejoin="round"/>
    <path d="M38 58 V104" stroke="#f2b233" stroke-width="5"/>
  </svg>

  <span class="label" style="left:35px;top:174px">Beef Pho</span>
  <div class="photo photo--bowl" role="img" aria-label="Photo of a bowl of beef pho" style="left:30px;top:195px;width:150px;height:100px"></div>
  <span class="label" style="left:224px;top:193px">Beef Noodle Salad</span>
  <div class="photo photo--salad" role="img" aria-label="Photo of a beef noodle salad bowl" style="left:190px;top:215px;width:165px;height:100px"></div>
  <div class="photo photo--bowl" role="img" aria-label="Photo of a bowl of chicken pho" style="left:58px;top:295px;width:152px;height:100px"></div>
  <span class="label" style="left:60px;top:398px">Chicken Pho</span>
  <div class="photo photo--salad" role="img" aria-label="Photo of a chicken noodle salad bowl" style="left:215px;top:315px;width:165px;height:108px"></div>
  <span class="label" style="left:232px;top:424px">Chicken Noodle Salad</span>

  <div class="ribbon ribbon--mains">Choose any<span class="ribbon__fold ribbon__fold--right"></span></div>
  <p class="choice choice--pho">Pho <span class="choice--or">OR</span></p>
  <p class="choice choice--salads">Noodle Salads</p>

  <div class="ribbon ribbon--sides">Choose any<span class="ribbon__fold ribbon__fold--left"></span></div>
  <span class="label" style="left:270px;top:505px">Spring Rolls</span>
  <div class="photo photo--plate" role="img" aria-label="Photo of fried spring rolls on a white plate" style="left:265px;top:522px;width:185px;height:105px"></div>
  <span class="label" style="left:498px;top:530px">Ricepaper Rolls</span>
  <div class="photo photo--board" role="img" aria-label="Photo of ricepaper rolls on a wooden board" style="left:425px;top:552px;width:180px;height:100px"></div>
  <p class="choice choice--spring">Spring Rolls</p>
  <p class="choice choice--spring-count">(<span class="count">5</span> rolls)</p>
  <p class="choice choice--or choice--sides-or">OR</p>
  <p class="choice choice--ricepaper">Ricepaper Rolls</p>
  <p class="choice choice--ricepaper-count">(<span class="count">2</span> rolls)</p>

  <div class="ribbon ribbon--drinks">Choose any<span class="ribbon__fold ribbon__fold--right"></span></div>
  <div class="photo photo--bottle" role="img" aria-label="Photo of a Cedar Ridge Water bottle" style="left:505px;top:655px;width:72px;height:175px"></div>
  <div class="price">$19.50</div>
  <p class="drinks">Cans <span class="drinks__or">OR</span> Water</p>

  <svg class="guides" viewBox="0 0 622 880" aria-hidden="true">
    <g fill="none" stroke="#fff" stroke-width="3" stroke-dasharray="14 9">
      <path d="M485 435 C470 490 420 490 340 478 C260 462 190 462 150 488"/>
      <path d="M100 645 C110 700 200 700 270 698 C330 696 360 705 372 717"/>
      <path d="M215 790 C245 795 280 792 300 780"/>
    </g>
  </svg>
</section>

<section class="poster poster--timber" aria-label="Bowl-erific Deal poster, timber edition">
  <svg class="frame" viewBox="0 0 622 880" aria-hidden="true">
    <path d="M50 45 H15 V853 H608 V45 H432" fill="none" stroke="#fff" stroke-width="3"/>
  </svg>
  <h2 class="title title__top">Bowl-erific</h2>
  <p class="title title__bottom">Deal</p>
  <svg class="thumb" viewBox="0 0 115 120" aria-hidden="true">
    <path d="M10 55 H38 L55 18 C58 8 72 8 72 22 L68 45 H100 C110 45 112 58 104 62 C112 66 110 78 101 79 C108 83 106 95 97 95 C102 100 98 110 90 110 H45 L38 104 H10 Z" fill="none" stroke="#f2b233" stroke-width="5" stroke-linejoin="round"/>
    <path d="M38 58 V104" stroke="#f2b233" stroke-width="5"/>
  </svg>

  <span class="label" style="left:35px;top:174px">Beef Pho</span>
  <div class="photo photo--bowl" role="img" aria-label="Photo of a bowl of beef pho" style="left:30px;top:195px;width:150px;height:100px"></div>
  <span class="label" style="left:224px;top:193px">Beef Noodle Salad</span>
  <div class="photo photo--salad" role="img" aria-label="Photo of a beef noodle salad bowl" style="left:190px;top:215px;width:165px;height:100px"></div>
  <div class="photo photo--bowl" role="img" aria-label="Photo of a bowl of chicken pho" style="left:58px;top:295px;width:152px;height:100px"></div>
  <span class="label" style="left:60px;top:398px">Chicken Pho</span>
  <div class="photo photo--salad" role="img" aria-label="Photo of a chicken noodle salad bowl" style="left:215px;top:315px;width:165px;height:108px"></div>
  <span class="label" style="left:232px;top:424px">Chicken Noodle Salad</span>

  <div class="ribbon ribbon--mains">Choose any<span class="ribbon__fold ribbon__fold--right"></span></div>
  <p class="choice choice--pho">Pho <span class="choice--or">OR</span></p>
  <p class="choice choice--salads">Noodle Salads</p>

  <div class="ribbon ribbon--sides">Choose any<span class="ribbon__fold ribbon__fold--left"></span></div>
  <span class="label" style="left:270px;top:505px">Spring Rolls</span>
  <div class="photo photo--plate" role="img" aria-label="Photo of fried spring rolls on a white plate" style="left:265px;top:522px;width:185px;height:105px"></div>
  <span class="label" style="left:498px;top:530px">Ricepaper Rolls</span>
  <div class="photo photo--board" role="img" aria-label="Photo of ricepaper rolls on a wooden board" style="left:425px;top:552px;width:180px;height:100px"></div>
  <p class="choice choice--spring">Spring Rolls</p>
  <p class="choice choice--spring-count">(<span class="count">5</span> rolls)</p>
  <p class="choice choice--or choice--sides-or">OR</p>
  <p class="choice choice--ricepaper">Ricepaper Rolls</p>
  <p class="choice choice--ricepaper-count">(<span class="count">2</span> rolls)</p>

  <div class="ribbon ribbon--drinks">Choose any<span class="ribbon__fold ribbon__fold--right"></span></div>
  <div class="photo photo--bottle" role="img" aria-label="Photo of a Cedar Ridge Water bottle" style="left:505px;top:655px;width:72px;height:175px"></div>
  <div class="price">$19.50</div>
  <p class="drinks">Cans <span class="drinks__or">OR</span> Water</p>

  <svg class="guides" viewBox="0 0 622 880" aria-hidden="true">
    <g fill="none" stroke="#fff" stroke-width="3" stroke-dasharray="14 9">
      <path d="M485 435 C470 490 420 490 340 478 C260 462 190 462 150 488"/>
      <path d="M100 645 C110 700 200 700 270 698 C330 696 360 705 372 717"/>
      <path d="M215 790 C245 795 280 792 300 780"/>
    </g>
  </svg>
</section>

</body>
</html>
```